Lanternleaf - Fresh Asian Cuisine Menu

We need to redo our menu to include pictures of food items. Our restaurant is vibrant, trendy, upscale Chinese cuisine

Requirements
Must have
• Must fit on 8.5x11 paper. We can remove the About Us section if needed but menu cannot be more than 6 pages total. Must include pictures of menu items

```html
<!DOCTYPE html>
<html lang="en">
<head>
<meta charset="utf-8">
<title>Lanternleaf - Fresh Asian Cuisine — Our Story</title>
<link rel="stylesheet" href="https://fonts.googleapis.com/css2?family=Noto+Serif:wght@400;700&display=swap">
<style>
  :root {
    --paper: #ffffff;
    --ink: #111111;
    --accent-red: #e0252b;
    --photo-red: #8a2a1c;
    --photo-cloth: #a89cae;
  }
  * { box-sizing: border-box; margin: 0; padding: 0; }
  html, body {
    width: 927px;
    height: 1200px;
    overflow: hidden;
    background: var(--paper);
  }
  .page {
    position: relative;
    width: 927px;
    height: 1200px;
    font-family: "Noto Serif", Georgia, serif;
    color: var(--ink);
  }
  .page-frame {
    position: absolute;
    left: 34px;
    top: 86px;
    width: 858px;
    height: 1082px;
    border: 2px dotted var(--accent-red);
  }
  .brand {
    position: absolute;
    left: 50%;
    top: 86px;
    transform: translate(-50%, -50%);
    display: flex;
    align-items: center;
    gap: 10px;
    padding: 0 14px;
    background: var(--paper);
  }
  .brand-dot {
    width: 22px;
    height: 22px;
    border-radius: 50%;
    background: var(--accent-red);
  }
  .brand-name {
    font-size: 20px;
    font-weight: 700;
    color: var(--ink);
  }
  .section-title {
    position: absolute;
    top: 176px;
    left: 0;
    width: 100%;
    text-align: center;
    font-size: 27px;
    font-weight: 700;
  }
  .story {
    position: absolute;
    left: 205px;
    top: 268px;
    width: 522px;
    font-size: 12.3px;
    line-height: 21.8px;
    hyphens: auto;
  }
  .story p + p { margin-top: 21.8px; }
  .feature-dish {
    position: absolute;
    left: 205px;
    top: 636px;
    width: 516px;
    height: 343px;
    background: linear-gradient(90deg, var(--photo-cloth) 0%, var(--photo-red) 40%, var(--photo-red) 60%, var(--photo-cloth) 100%);
  }
</style>
</head>
<body>
  <main class="page">
    <div class="page-frame"></div>

    <div class="brand">
      <span class="brand-dot"></span>
      <span class="brand-name">Lanternleaf</span>
    </div>

    <h1 class="section-title">OUR STORY</h1>

    <section class="story">
      <p>At Lanternleaf, we pride ourselves in serving fresh, authentic Sichuan Chinese cuisine delicately prepared by our expertly trained Chefs.</p>
      <p>Sichuan cuisine originates from southwest China between the Sichuan Basin and Tibetan Plateau. It is known for being both very spicy and flavorful, much like our own southern Louisiana cuisine.</p>
      <p>Our Executive Chef, Wei Tang grew up in the southwestern Chinese province of Sichuan, China where he began his training at fifteen years old under his grandfather’s mentorship. Chef Tang became an acclaimed chef in his province, opening several restaurants and traveling throughout China to cater for many of China’s elite. His dream was to share his Sichuan style with the world which lead him to the United States. He has worked in restaurants in both Houston and New York and we now welcome him to his new home in Lafayette, Louisiana.</p>
    </section>

    <div class="feature-dish" role="img" aria-label="Photo of a bowl of spicy Sichuan beef with dried red chilies and cilantro"></div>
  </main>
</body>
</html>
```